Lantern Business Cards

Need business cards for my employees at my restaurant.

Needs to include:
Our Logo
Lantern Bowls & Brews
Name: Nora Pettigrew
Title : Owner
Address: 487 Mirella Ave. Lake Havasu City, AZ 86519
Web: www.lanternkestrel.com
Phone: 928-555-0147
Cell: 928-555-0192
Email: info@lanternkestrel.com

```html
<!DOCTYPE html>
<html lang="en">
<head>
<meta charset="utf-8">
<title>Lantern Bowls &amp; Brews – Business Cards</title>
<link href="https://fonts.googleapis.com/css2?family=Montserrat:wght@400;500;700;800&display=swap" rel="stylesheet">
<style>
  :root {
    --page: #d9d9db;
    --card-black: #161617;
    --card-black-2: #232325;
    --brand-red: #c8202f;
    --white: #ffffff;
  }
  * { box-sizing: border-box; margin: 0; padding: 0; }
  html, body { width: 1200px; height: 874px; overflow: hidden; }
  body {
    background: var(--page);
    font-family: "Montserrat", sans-serif;
    position: relative;
  }
  .card {
    position: absolute;
    left: 280px;
    width: 640px;
    height: 366px;
    border-radius: 22px;
    overflow: hidden;
    background: var(--card-black);
    box-shadow: 0 10px 26px rgba(0,0,0,.25);
  }
  .card--back { top: 40px; background: linear-gradient(135deg, var(--card-black-2), var(--card-black) 60%); }
  .card--front { top: 456px; }

  .back-emblem {
    position: absolute; left: 40px; top: 20px;
    width: 300px; height: 300px; border-radius: 50%;
    background: radial-gradient(circle at 35% 30%, #6a6a6c, #2a2a2c 70%);
    opacity: .55;
  }

  .wordmark {
    position: absolute;
    display: flex; flex-direction: column; align-items: center;
  }
  .wordmark__name {
    color: var(--brand-red);
    font-weight: 800;
    letter-spacing: 2px;
    line-height: 1;
  }
  .wordmark__tag {
    display: flex; align-items: center; gap: 8px;
    color: var(--white);
    font-weight: 500;
    letter-spacing: 1.5px;
    text-transform: uppercase;
    margin-top: 4px;
  }
  .wordmark__tag::before, .wordmark__tag::after {
    content: ""; width: 30px; height: 1.5px; background: var(--white);
  }
  .card--back .wordmark { right: 34px; bottom: 34px; }
  .card--back .wordmark__name { font-size: 46px; }
  .card--back .wordmark__tag { font-size: 9px; }

  .logo-row { position: absolute; left: 28px; top: 22px; display: flex; align-items: center; gap: 14px; }
  .logo-dot { width: 62px; height: 62px; border-radius: 50%; background: var(--brand-red); }
  .logo-row .wordmark { position: static; }
  .logo-row .wordmark__name { font-size: 46px; }
  .logo-row .wordmark__tag { font-size: 9px; }

  .contact {
    position: absolute; left: 30px; top: 106px;
    color: var(--white); font-size: 15px; line-height: 1.4;
    z-index: 2;
  }
  .contact__address { margin-bottom: 2px; }
  .contact__line { display: flex; align-items: center; gap: 8px; }
  .contact__line svg { width: 13px; height: 13px; fill: var(--brand-red); flex: none; }

  .person { position: absolute; right: 0; top: 116px; display: flex; align-items: stretch; }
  .person__text { text-align: right; padding-right: 14px; }
  .person__name { color: var(--brand-red); font-weight: 700; font-size: 28px; line-height: 1.1; }
  .person__title { color: var(--white); font-size: 16px; margin-top: 2px; }
  .person__bar { width: 16px; background: var(--brand-red); }

  .wave { position: absolute; left: 0; bottom: 0; width: 640px; height: 126px; }
  .front-emblem {
    position: absolute; right: 70px; bottom: 30px;
    width: 160px; height: 160px; border-radius: 50%;
    background: var(--white);
    border: 10px solid var(--card-black);
  }
</style>
</head>
<body>

<section class="card card--back">
  <div class="back-emblem" role="img" aria-label="Large brand emblem area"></div>
  <div class="wordmark">
    <span class="wordmark__name">LANTERN</span>
    <span class="wordmark__tag">Bowls and Brews</span>
  </div>
</section>

<section class="card card--front">
  <svg class="wave" viewBox="0 0 640 126" preserveAspectRatio="none" aria-hidden="true">
    <path d="M0 0 C120 60 300 95 640 86 L640 126 L0 126 Z" fill="var(--white)"/>
    <path d="M0 22 C130 78 320 104 640 96 L640 126 L0 126 Z" fill="var(--brand-red)"/>
  </svg>

  <div class="logo-row">
    <div class="logo-dot"></div>
    <div class="wordmark">
      <span class="wordmark__name">LANTERN</span>
      <span class="wordmark__tag">Bowls and Brews</span>
    </div>
  </div>

  <div class="contact">
    <p class="contact__address">487 Mirella Ave. Lake<br>Havasu City, AZ 86519</p>
    <p class="contact__line">
      <svg viewBox="0 0 24 24"><path d="M6.6 10.8a15 15 0 0 0 6.6 6.6l2.2-2.2a1 1 0 0 1 1-.25 11.4 11.4 0 0 0 3.6.57 1 1 0 0 1 1 1V20a1 1 0 0 1-1 1A17 17 0 0 1 3 4a1 1 0 0 1 1-1h3.5a1 1 0 0 1 1 1c0 1.25.2 2.45.57 3.57a1 1 0 0 1-.25 1z"/></svg>
      928-555-0147</p>
    <p class="contact__line">
      <svg viewBox="0 0 24 24"><path d="M7 1h10a2 2 0 0 1 2 2v18a2 2 0 0 1-2 2H7a2 2 0 0 1-2-2V3a2 2 0 0 1 2-2zm0 3v14h10V4zm5 15.5a1 1 0 1 0 0 2 1 1 0 0 0 0-2z"/></svg>
      928-555-0192</p>
    <p class="contact__line">
      <svg viewBox="0 0 24 24"><path d="M2 5h20v14H2zm2 2v.5l8 5 8-5V7z"/></svg>
      info@lanternkestrel.com</p>
    <p class="contact__line">
      <svg viewBox="0 0 24 24"><path d="M12 2a10 10 0 1 0 0 20 10 10 0 0 0 0-20zm0 2c.9 1.2 1.6 2.8 2 4.5h-4c.4-1.7 1.1-3.3 2-4.5zM4.3 14a8 8 0 0 1 0-4h3.4a17 17 0 0 0 0 4zm.8 2h3c.4 1.5.9 2.8 1.6 3.8A8 8 0 0 1 5.1 16zm3-8h-3a8 8 0 0 1 4.6-3.8C8.9 5.2 8.4 6.5 8 8zm3.9 12c-.9-1.2-1.6-2.8-2-4.5h4c-.4 1.7-1.1 3.3-2 4.5zm2.3-6H9.8a15 15 0 0 1 0-4h4.4a15 15 0 0 1 0 4zm.1 5.8c.7-1 1.2-2.3 1.6-3.8h3a8 8 0 0 1-4.6 3.8zM16.3 14a17 17 0 0 0 0-4h3.4a8 8 0 0 1 0 4z"/></svg>
      www.lanternkestrel.com</p>
  </div>

  <div class="person">
    <div class="person__text">
      <p class="person__name">Nora Pettigrew</p>
      <p class="person__title">Owner</p>
    </div>
    <div class="person__bar"></div>
  </div>

  <div class="front-emblem" role="img" aria-label="Brand emblem area"></div>
</section>

</body>
</html>
```